依頼詳細
以前こちらで作成して頂いた雰囲気の内容でお願いします。
※添付チラシ

記載項目
・もえぎうたのロゴマークを入れてください。
https://moegiuta.or.jp/event-t/2020-03-14-2 このアドレス用のQRコードを記載してください。
・添付しました画像を使用してください。
サイズ
A4
ページ数
片面
希望イメージ
シンプル 複雑
単色 カラフル
暗い 明るい
日常 高級
遊び心 厳粛
未来的 伝統的
女性的 男性的
希望する色
納品ファイル
補足説明
■ 選んだ理由

ご提案いただきありがとうございました。
どれも良いご提案で悩みましたが、色合いや、雰囲気、読みやすさ、
これから家づくりを考える対象年齢層などを考慮して
選択させて頂きました。

■ 提案者全員のお礼・コメント

多くのご提案を頂きありがとうございました。<m(__)m>

```html
<!DOCTYPE html>
<html lang="ja">
<head>
<meta charset="utf-8">
<title>「家づくり」はじめの一歩 セミナー</title>
<link rel="stylesheet" href="https://fonts.googleapis.com/css2?family=Noto+Sans+JP:wght@400;500;700;900&family=Shippori+Mincho+B1:wght@700;800&display=swap">
<style>
:root{
  --green:#79b340;
  --green-dark:#4f8a25;
  --green-pale:#eef6e3;
  --orange:#ef8421;
  --brown:#4e4036;
  --gray:#6d645c;
  --red:#d8402f;
  --paper:#ffffff;
}
*{margin:0;padding:0;box-sizing:border-box}
html,body{width:846px;height:1200px;overflow:hidden;background:var(--paper)}
body{font-family:"Noto Sans JP",sans-serif;color:var(--brown);position:relative}
.flyer{position:absolute;inset:0;overflow:hidden}
.abs{position:absolute}

.plan-bg{left:0;top:0;width:846px;height:720px;background:linear-gradient(180deg,#f6f4f0 0%,#ffffff 70%)}
.leaves{left:520px;top:0;width:180px;height:120px;border-radius:0 0 0 90px;background:linear-gradient(135deg,#b9dc8a,#e3f1cf)}
.leaves-left{left:0;top:300px;width:40px;height:90px;border-radius:0 60px 60px 0;background:linear-gradient(135deg,#b9dc8a,#e8f4d8)}

.headline{left:40px;top:30px;font-family:"Shippori Mincho B1",serif;font-weight:800;color:var(--brown);line-height:1.1}
.headline .l1{font-size:92px;letter-spacing:-4px;display:block;white-space:nowrap}
.headline .l2{font-size:84px;letter-spacing:-2px;display:block;border-bottom:4px solid var(--green);padding-bottom:6px;width:560px;white-space:nowrap}
.subtitle{left:60px;top:272px;font-size:28px;font-weight:700;color:var(--green-dark);letter-spacing:1px;white-space:nowrap}

.series{left:776px;top:12px;width:48px;height:284px;background:var(--green);color:#fff;writing-mode:vertical-rl;font-size:18px;font-weight:700;display:flex;align-items:center;justify-content:center;letter-spacing:1px;white-space:nowrap}
.catch{left:692px;top:40px;writing-mode:vertical-rl;font-size:30px;font-weight:900;color:var(--orange);line-height:1.35;letter-spacing:2px;white-space:nowrap}
.catch-sub{left:604px;top:60px;writing-mode:vertical-rl;font-size:15px;color:var(--gray);line-height:1.7;font-weight:500;white-space:nowrap}

.photo{left:380px;top:370px;width:466px;height:310px;background:linear-gradient(135deg,#efe6da 0%,#e4d5c2 50%,#f3efe8 100%)}

.badge{width:104px;height:104px;border-radius:50%;background:var(--orange);color:#fff;display:flex;align-items:center;justify-content:center;text-align:center;font-weight:900;font-size:17px;line-height:1.25;border:4px solid #fff;box-shadow:0 0 0 2px var(--orange);white-space:nowrap}
.badge-kids{left:700px;top:425px}
.badge-free{left:640px;top:515px;font-size:20px}

.intro{left:50px;top:318px;width:320px;font-size:14px;line-height:1.62;color:var(--brown);white-space:nowrap}
.intro em{font-style:normal;color:var(--red);font-weight:700}
.intro b{font-weight:700}

.lecturer{left:50px;top:716px;width:310px;height:50px;background:var(--green);color:#fff;font-size:16px;font-weight:700;line-height:1.3;padding:5px 12px;text-align:center;border-radius:4px;white-space:nowrap}
.lecturer span{color:#fff9c4}

.contents{left:50px;top:772px;width:310px;height:228px;border:2px solid var(--green);border-radius:4px;background:#fff;padding:8px 14px}
.contents h3{background:var(--green);color:#fff;font-size:15px;text-align:center;border-radius:14px;margin:0 30px 6px;padding:2px 0}
.contents ul{list-style:none}
.contents li{font-size:15px;font-weight:700;line-height:1.6;padding-left:20px;position:relative;white-space:nowrap}
.contents li::before{content:"";position:absolute;left:2px;top:8px;width:10px;height:10px;background:var(--green);border-radius:2px}

.date{left:440px;top:700px;width:390px;color:var(--orange);white-space:nowrap}
.date .year{font-size:30px;font-weight:900;display:block;margin-left:60px;line-height:1}
.date .md{font-size:108px;font-weight:900;letter-spacing:-4px;line-height:.95}
.date .dow{display:inline-flex;width:66px;height:66px;border-radius:50%;background:var(--orange);color:#fff;font-size:21px;font-weight:900;align-items:center;justify-content:center;vertical-align:top;margin-top:20px;margin-left:6px}
.time{left:470px;top:846px;font-size:19px;font-weight:700;color:var(--brown);white-space:nowrap}

.venue{left:455px;top:878px;width:370px;height:60px;background:var(--green-pale);border-left:10px solid var(--green);display:flex;align-items:center;padding-left:22px;font-size:42px;font-weight:900;color:var(--green-dark);letter-spacing:4px;white-space:nowrap}
.address{left:470px;top:944px;font-size:13px;color:var(--gray);white-space:nowrap}

.fee{left:455px;top:970px;width:370px;display:flex;align-items:center;gap:10px;white-space:nowrap}
.fee .tag{background:var(--green);color:#fff;font-size:16px;font-weight:700;padding:4px 10px;border-radius:3px}
.fee .val{font-size:34px;font-weight:900;color:var(--orange);margin-right:16px}
.fee .val small{font-size:22px}

.apply{left:40px;top:1010px;width:420px;height:138px;border:2px solid var(--orange);border-radius:6px;background:#fff;padding:8px 16px}
.apply .head{display:flex;gap:10px;align-items:center;white-space:nowrap}
.apply .head .tag{background:var(--orange);color:#fff;font-weight:700;font-size:16px;padding:2px 10px;border-radius:3px}
.apply .head .hours{font-size:13px;color:var(--gray)}
.apply .note{font-size:13px;color:var(--gray);margin-top:2px;white-space:nowrap}
.apply .tel{display:flex;align-items:center;gap:8px;font-size:42px;font-weight:900;color:var(--orange);line-height:1.1;letter-spacing:1px;white-space:nowrap}
.apply .tel svg{flex:none}
.apply .fax{font-size:15px;font-weight:700;color:var(--brown);white-space:nowrap}

.web{left:485px;top:1034px;width:110px;font-size:13px;font-weight:700;color:var(--green-dark);line-height:1.4;text-align:center;border:2px solid var(--green);border-radius:6px;padding:8px 4px}

.organizer{left:40px;top:1156px;font-size:13px;color:var(--gray);white-space:nowrap}
.brand-org{left:630px;top:1090px;font-size:12px;color:var(--gray);white-space:nowrap}
.brand{left:630px;top:1110px;display:flex;align-items:center;gap:10px;white-space:nowrap}
.brand .mark{width:26px;height:26px;border-radius:50%;background:var(--green);flex:none}
.brand .name{font-size:30px;font-weight:900;color:var(--green-dark);letter-spacing:2px}

.bottom-band{left:0;top:1186px;width:846px;height:14px;background:var(--green)}
</style>
</head>
<body>
<main class="flyer">
  <div class="abs plan-bg" role="img" aria-label="淡い住宅の間取り図の背景"></div>
  <div class="abs leaves" role="img" aria-label="緑の葉のイラスト"></div>
  <div class="abs leaves-left" role="img" aria-label="緑の葉のイラスト"></div>

  <h1 class="abs headline"><span class="l1">「家づくり」</span><span class="l2">はじめの一歩</span></h1>
  <p class="abs subtitle">～後悔しないために学ぶ2つの準備～</p>

  <div class="abs series">暮らしの「学び場」セミナー</div>
  <p class="abs catch">家づくりを始める前に<br>知っておくべきこと</p>
  <p class="abs catch-sub">住まいの計画は、最初の一歩で<br>大きく変わります。知っておくべき<br>ことを、わかりやすくお伝えします。</p>

  <div class="abs photo" role="img" aria-label="新居の前で笑顔の家族の写真"></div>

  <div class="abs badge badge-kids">お子様連れ<br>OK</div>
  <div class="abs badge badge-free">参加費<br>無料</div>

  <div class="abs intro">
    <p>家を建てようと決めた人は<br>
    まず何から始めればよいのか、<br>
    悩まれる方も多いと思います。<br>
    住まいの計画には<b>資金計画</b>と<br>
    <b>家族の話し合い</b>がとても大切です。<br>
    準備が不十分なまま進めると、<br>
    あとで<em>「こんなはずでは…」</em>と<br>
    後悔することにもなりかねません。<br>
    本セミナーでは、家づくりの<br>
    <em>「なにから・どうやって始めればよいか」</em><br>
    を、専門の講師が丁寧にお話しします。<br>
    <b>「もっと早く知りたかった」</b>の声も。<br>
    <em>「夫婦（家族）で話し合っておくこと」</em><br>
    <em>「計画を進める順番」</em><br>
    <em>「何をどう選べばよいか」</em><br>
    を一緒に学び、納得できる<br>
    家づくりを始めてみませんか。</p>
  </div>

  <div class="abs lecturer"><span>もえぎうた認定講師</span>が<br>わかりやすく説明します</div>

  <section class="abs contents">
    <h3>セミナー内容</h3>
    <ul>
      <li>暮らすスペースはたった3種類</li>
      <li>住宅購入を失敗する5つの原因</li>
      <li>土地を探すときの注意点</li>
      <li>固定資産税に気をつけること</li>
      <li>保険を使う際に必要なこと</li>
      <li>住宅ローンの選び方と返済計画</li>
      <li>自分の「住宅予算」の出し方</li>
    </ul>
  </section>

  <div class="abs date"><span class="year">2020</span><span class="md">3/14</span><span class="dow">SAT</span></div>
  <p class="abs time">13:30～15:30 ｜ 受付 13:00～</p>

  <div class="abs venue">森野の家</div>
  <p class="abs address">緑ヶ丘市中央区桜町3丁目 4-8</p>

  <div class="abs fee">
    <span class="tag">受講料</span><span class="val">無料</span>
    <span class="tag">定員</span><span class="val">10<small>名</small></span>
  </div>

  <section class="abs apply">
    <div class="head"><span class="tag">参加申込</span><span class="hours">受付時間 平日 9:00～17:00</span></div>
    <p class="note">電話・ホームページにてお申し込みください。</p>
    <div class="tel">
      <svg width="40" height="40" viewBox="0 0 40 40" aria-hidden="true"><rect width="40" height="40" rx="6" fill="#ef8421"/><path d="M13 9c2 0 3 4 3 6s-2 2-2 3c1 3 4 6 7 7 1 0 1-2 3-2s6 1 6 3-2 5-5 5C16 31 9 24 9 15c0-3 2-6 4-6z" fill="#fff"/></svg>
      0120-000-123
    </div>
    <p class="fax">FAX 06-0000-4567</p>
  </section>

  <div class="abs web">WEBからの<br>お申込みは<br>こちら</div>

  <p class="abs organizer">（主催）もえぎうた（一般社団法人 暮らしの学び場）</p>
  <p class="abs brand-org">一般社団法人 暮らしの学び場</p>
  <div class="abs brand"><span class="mark"></span><span class="name">もえぎうた</span></div>

  <div class="abs bottom-band"></div>
</main>
</body>
</html>
```